In need of an AWESOME website for our Water Re-filling Store

The project is to design a website for our retail store front with the website www.brookvalefillhouse.com. Currently if you go to that site it redirects you to our other site www.brookvalebottleworks.com which is just our water bottle website. So, I need a new website created for www.brookvalefillhouse.com (retail storefront)
Use our Squarespace to create a site with pages to help educate, tell about us, link to our water bottle brand site that is already created with Squarespace, and show the family and community aspects that we believe in. Our current water bottle website is www.brookvalebottleworks.com for reference
We also sell hydration products, especially QRVX products and have access to digital media through our QRVX dealer site. we sell bottles, dispensers and other supplies for water refilling customers. We sell Ice as well.

Target Market(s)

Local residents looking to fill up their 1-5 gallon water jugs

Industry/Entity Type

Alkaline and Purified Water Retail Re-filling Store

Coding

Coded - Design and coding required

Font styles to use
Serif
Sans Serif

Colors
0054AA
0677BA
7BADD7
CADEEF
E8F1F8

Requirements
Must have
• pictures of our family in the about us section and pictures of our store inside and out.

```html
<!DOCTYPE html>
<html lang="en">
<head>
<meta charset="utf-8">
<title>Brookvale Fill House</title>
<link href="https://fonts.googleapis.com/css2?family=Inter:wght@400;500;600;700;800&family=Roboto+Slab:wght@300;500;600&display=swap" rel="stylesheet">
<style>
:root{
  --blue:#0054AA;
  --blue-mid:#0677BA;
  --blue-soft:#7BADD7;
  --blue-pale:#CADEEF;
  --blue-mist:#E8F1F8;
  --navy:#1b2460;
  --ink:#1b2233;
  --text:#2e3442;
  --white:#ffffff;
  --cyan:#12a4f0;
}
*{margin:0;padding:0;box-sizing:border-box}
html,body{width:1200px;height:3045px;overflow:hidden}
body{position:relative;font-family:"Inter",sans-serif;color:var(--text);background:#eef3f8}
.abs{position:absolute}
a{color:inherit;text-decoration:none}

/* header */
.brand{left:144px;top:14px;width:110px;font-weight:700;font-size:17px;line-height:1.1;color:var(--blue);text-align:center}
.brand small{display:block;font-size:9px;font-weight:500;margin-top:3px}
.nav{top:33px;left:0;width:1200px;height:14px;font-size:10px;font-weight:500;color:var(--ink)}
.nav a{position:absolute;top:0}
.nav .active{color:var(--blue-mid);border-bottom:1px solid var(--blue-mid);padding-bottom:4px}
.head-phone{left:855px;top:26px;display:flex;align-items:center;gap:6px;font-size:13px;font-weight:500;color:var(--ink)}
.dot{width:26px;height:26px;border-radius:50%;background:var(--blue);display:flex;align-items:center;justify-content:center}
.social{width:26px;height:26px;border-radius:50%;background:var(--blue)}

/* hero */
.hero-bg{left:0;top:0;width:1200px;height:545px;background:linear-gradient(180deg,#dfe9f3 0%,#eaf1f8 40%,#f4f7fb 75%,#eef3f8 100%)}
.hero-title{left:176px;top:213px;font-size:39px;font-weight:600;line-height:38px;color:var(--ink);letter-spacing:-.5px}
.hero-title strong{color:var(--blue);font-weight:800}
.hero-text{left:177px;top:347px;width:330px;font-size:12.5px;line-height:17px;color:var(--ink)}
.btn{display:flex;align-items:center;justify-content:center;border-radius:20px;font-size:9.5px;font-weight:700;letter-spacing:.3px}
.btn-fill{background:var(--blue);color:var(--white)}
.btn-line{border:1px solid var(--blue);color:var(--ink);background:transparent}
.arrow{width:24px;height:24px;border-radius:50%;background:var(--white);box-shadow:0 1px 4px rgba(0,0,0,.15);display:flex;align-items:center;justify-content:center}
.hero-art{left:567px;top:112px;width:461px;height:414px;border-radius:40% 40% 20% 20%;background:radial-gradient(ellipse at 55% 45%,#2f7ee0 0%,#8ab8e8 45%,rgba(220,232,244,0) 72%)}

/* features */
.feat-frame{left:210px;top:579px;width:779px;height:301px;background:rgba(255,255,255,.8);border-radius:8px;box-shadow:0 6px 24px rgba(0,60,140,.1)}
.feat{left:223px;top:592px;width:755px;height:277px;background:radial-gradient(ellipse at 50% 10%,#2f82d8 0%,#0f5ec0 45%,#0b4aa6 100%);color:var(--white)}
.feat h2{position:absolute;top:44px;left:0;width:100%;text-align:center;font-size:27px;font-weight:600;line-height:29px;letter-spacing:-.3px}
.feat-item{position:absolute;top:122px;width:170px;text-align:center}
.feat-item svg{display:block;margin:0 auto 14px}
.feat-item h3{font-size:14px;font-weight:600;margin-bottom:8px}
.feat-item p{font-size:10.5px;line-height:15px;color:#dbe8f7}

/* about */
.about-photo{left:0;top:934px;width:526px;height:449px;background:linear-gradient(160deg,#e9eef4 0%,#cfdde9 45%,#c9b79c 100%)}
.about-ring{left:130px;top:957px;width:284px;height:284px;border:1.5px solid var(--blue-mid);border-radius:50%}
.eyebrow{font-size:10.5px;font-weight:600;letter-spacing:1px;color:var(--blue-mid)}
.about-title{left:600px;top:979px;font-size:32px;font-weight:600;line-height:32px;color:var(--ink);letter-spacing:-.4px}
.about-title strong{color:var(--blue);font-weight:800}
.about-text{left:600px;top:1087px;width:366px;font-size:12px;line-height:17.1px;color:var(--ink)}

/* products */
.prod-head{left:0;top:1448px;width:1200px;text-align:center}
.prod-head h2{margin-top:10px;font-size:31px;font-weight:500;line-height:32px;color:var(--ink);letter-spacing:-.4px}
.prod-wave{left:0;top:1620px;width:1200px;height:664px}
.prod{position:absolute;top:1561px;width:240px;text-align:center}
.ring{width:134px;height:134px;border-radius:50%;border:3px solid var(--blue);margin:0 auto;display:flex;align-items:center;justify-content:center;background:var(--white)}
.prod h3{margin-top:18px;font-size:16px;font-weight:600;color:var(--ink)}
.prod p{margin-top:6px;font-size:10.5px;line-height:16.5px;color:var(--text)}

/* process */
.process-title{left:0;top:1972px;width:1200px;text-align:center;font-size:32px;font-weight:500;line-height:36px;color:var(--white);letter-spacing:-.3px}
.step{position:absolute;top:2083px;width:232px;height:272px;background:linear-gradient(180deg,#2f7fcc 0%,#2a78c6 100%);box-shadow:0 8px 20px rgba(0,40,100,.25);text-align:center;color:var(--white)}
.step-head{display:flex;align-items:center;justify-content:center;gap:4px;height:56px;margin-top:24px}
.step-label{font-size:8px;line-height:10px;font-weight:500;letter-spacing:.3px;color:#e4efff}
.step-num{font-family:"Roboto Slab",serif;font-size:52px;font-weight:300;line-height:56px;color:transparent;-webkit-text-stroke:1.3px #e4efff}
.step h3{margin-top:10px;font-family:"Roboto Slab",serif;font-size:15.5px;font-weight:500;line-height:20px;letter-spacing:.2px;white-space:nowrap}
.step p{margin:16px auto 0;width:170px;font-size:10px;line-height:16px;color:#e1ecf8}
.step-icon{width:48px;height:48px;border-radius:50%;border:2px solid var(--white);margin:26px auto 0;display:flex;align-items:center;justify-content:center}
.step-icon i{width:30px;height:30px;border-radius:50%;background:var(--white);display:block}

/* showcase */
.big-word{left:0;top:2578px;width:1200px;text-align:center;white-space:nowrap;font-size:80px;line-height:80px;font-weight:800;letter-spacing:-1px;color:#d3e1f0}
.show-disc{left:484px;top:2372px;width:232px;height:232px;border-radius:50%;background:linear-gradient(180deg,#2468c9,#0c4ea8)}
.show-art{left:414px;top:2420px;width:337px;height:168px;border-radius:30px;background:radial-gradient(ellipse at 50% 50%,#e3edf8 0%,#9fc1e4 50%,rgba(159,193,228,0) 75%)}

/* footer */
.footer-wave{left:0;top:2630px;width:1200px;height:40px}
.footer{left:0;top:2664px;width:1200px;height:381px;background:var(--navy);color:var(--white)}
.cta{left:230px;top:2711px;font-size:21px;font-weight:500;color:var(--white);letter-spacing:-.3px}
.cta em{font-style:normal;color:var(--cyan)}
.cta-btn{left:758px;top:2704px;width:148px;height:41px;border-radius:21px;background:var(--cyan);display:flex;align-items:center;gap:8px;padding-left:12px;font-size:12.5px;font-weight:500;color:var(--white)}
.foot-brand{left:230px;top:2818px;font-size:18px;font-weight:700;color:var(--white);line-height:1.1}
.foot-text{font-size:9.5px;line-height:15px;color:#e2e6f3}
.foot-h{font-size:12px;font-weight:600;letter-spacing:.2px;color:var(--white)}
.foot-list{list-style:none;font-size:9.5px;color:#e2e6f3}
.foot-list li{height:24px}
.foot-row{display:flex;align-items:flex-start;gap:6px}
.copy{left:230px;top:3012px;font-size:9.5px;color:#cfd5ea}
</style>
</head>
<body>

<!-- hero -->
<div class="abs hero-bg" role="img" aria-label="Snowy mountain landscape above a calm lake"></div>
<div class="abs hero-art" role="img" aria-label="Branded aluminium bottle and five-gallon water jug among ice cubes and mint leaves"></div>

<div class="abs brand">Brookvale<br>Bottle Works<small>“Stay Healthy and Hydrated”</small></div>

<nav class="abs nav">
  <a class="active" style="left:405px">HOME</a>
  <a style="left:460px">ABOUT US</a>
  <a style="left:534px">OUR PRODUCT</a>
  <a style="left:630px">BLOG</a>
  <a style="left:681px">CONTACT</a>
</nav>

<div class="abs head-phone">
  <span class="dot"><svg width="13" height="13" viewBox="0 0 24 24"><path d="M6.6 10.8a15.1 15.1 0 0 0 6.6 6.6l2.2-2.2c.3-.3.7-.4 1-.2 1.1.4 2.3.6 3.6.6.6 0 1 .4 1 1V20c0 .6-.4 1-1 1A17 17 0 0 1 3 4c0-.6.4-1 1-1h3.5c.6 0 1 .4 1 1 0 1.3.2 2.5.6 3.6.1.3 0 .7-.2 1z" fill="#fff"/></svg></span>
  555-014-2730
</div>
<span class="abs social" style="left:991px;top:25px"></span>
<span class="abs social" style="left:1029px;top:25px"></span>

<h1 class="abs hero-title">Always Want Safe<br>And Good Water For<br><strong>Healthy Life.</strong></h1>
<p class="abs hero-text"><b>Brookvale Bottle Works.</b> bottles ultra-purified alkaline water that is pH 9+ to support optimal hydration and whole-body wellness.</p>
<a class="abs btn btn-fill" style="left:178px;top:415px;width:123px;height:34px">MORE ABOUT US</a>
<a class="abs btn btn-line" style="left:306px;top:415px;width:110px;height:34px">CONTACT US</a>
<span class="abs arrow" style="left:178px;top:489px"><svg width="10" height="10" viewBox="0 0 10 10"><path d="M9 5H1M4 2 1 5l3 3" fill="none" stroke="#1b2233" stroke-width="1.2"/></svg></span>
<span class="abs arrow" style="left:209px;top:489px"><svg width="10" height="10" viewBox="0 0 10 10"><path d="M1 5h8M6 2l3 3-3 3" fill="none" stroke="#1b2233" stroke-width="1.2"/></svg></span>

<!-- features -->
<div class="abs feat-frame"></div>
<section class="abs feat">
  <h2>Healthy Mineral Water for You &amp;<br>Your Family</h2>
  <div class="feat-item" style="left:14px">
    <svg width="40" height="42" viewBox="0 0 40 42" fill="none" stroke="#fff" stroke-width="1.6"><path d="M20 3c6 9 9 14 9 19a9 9 0 0 1-18 0c0-5 3-10 9-19z"/><ellipse cx="20" cy="36" rx="16" ry="4"/></svg>
    <h3>Maxium Purity</h3><p>Lorem ipsum dolor sit amet<br>adipiscing elit</p>
  </div>
  <div class="feat-item" style="left:196px">
    <svg width="40" height="42" viewBox="0 0 40 42" fill="none" stroke="#fff" stroke-width="1.6"><path d="M20 4c4 6 6 9 6 12a6 6 0 0 1-12 0c0-3 2-6 6-12z"/><path d="M4 20l5 14h8v-8l-5-6M36 20l-5 14h-8v-8l5-6"/></svg>
    <h3>Cholorine Free</h3><p>Lorem ipsum dolor sit amet<br>cons ectetur</p>
  </div>
  <div class="feat-item" style="left:374px">
    <svg width="40" height="42" viewBox="0 0 40 42" fill="none" stroke="#fff" stroke-width="1.6"><path d="M16 8l4-5 4 5M13 14l-8 14M27 14l8 14M10 36h20M24 8l4 7M5 28l3 8M35 28l-3 8"/></svg>
    <h3>Filtration</h3><p>Lorem ipsum dolor sit amet<br>cons ectetur</p>
  </div>
  <div class="feat-item" style="left:558px">
    <svg width="40" height="42" viewBox="0 0 40 42" fill="none" stroke="#fff" stroke-width="1.6"><rect x="16" y="2" width="8" height="5"/><path d="M15 7h10l2 5v27H13V12z"/><path d="M20 20c2 3 3 4 3 6a3 3 0 0 1-6 0c0-2 1-3 3-6z"/></svg>
    <h3>Healthy Water</h3><p>Lorem ipsum dolor sit amet cons<br>ectetur adipiscing elit</p>
  </div>
</section>

<!-- about -->
<div class="abs about-photo" role="img" aria-label="Woman in a white shirt drinking from a branded bottle on a beach"></div>
<div class="abs about-ring"></div>
<p class="abs eyebrow" style="left:600px;top:956px">ABOUT US</p>
<h2 class="abs about-title">We Are Focused On<br>Making Your <strong>Process A<br>Success</strong></h2>
<p class="abs about-text">Brookvale Bottle Works bottles ultra-purified alkaline water that is pH 9+ to support optimal hydration and whole-body wellness. Alkaline water is believed to help neutralize acid in the body, improve hydration at the cellular level, and support athletic performance and recovery. Every drop is filtered through a multi-stage process to remove impurities and enhance mineral content, ensuring a crisp, clean taste with every sip. Whether you're pushing through an intense workout or staying sharp during a busy day, our water is formulated to refresh, rehydrate, and rejuvenate you from the inside out.</p>
<a class="abs btn btn-fill" style="left:603px;top:1277px;width:122px;height:33px">MORE ABOUT US</a>

<!-- blue process band with white wave -->
<svg class="abs prod-wave" viewBox="0 0 1200 664" preserveAspectRatio="none">
  <defs><linearGradient id="sea" x1="0" y1="0" x2="0" y2="1"><stop offset="0" stop-color="#0b4fae"/><stop offset=".5" stop-color="#0e5cc0"/><stop offset="1" stop-color="#0a4aa5"/></linearGradient></defs>
  <rect width="1200" height="664" fill="url(#sea)"/>
  <path d="M0 0H1200V35C1160 120 1120 200 1010 230 900 258 790 210 700 235 620 258 560 268 470 240 380 210 300 170 180 150 90 130 30 100 0 70Z" fill="#eff3f8"/>
</svg>

<!-- products -->
<div class="abs prod-head">
  <p class="eyebrow">OUR PRODUCT</p>
  <h2>You’ll Love Fresh<br>Taste of Our Natural Water</h2>
</div>
<div class="prod" style="left:211px">
  <div class="ring" style="border-color:#0d4ea8"><svg width="56" height="76" viewBox="0 0 56 76" fill="none" stroke="#0d4ea8" stroke-width="2.2"><rect x="20" y="3" width="16" height="8" rx="2"/><path d="M14 14h28l6 10v44a5 5 0 0 1-5 5H13a5 5 0 0 1-5-5V24z"/><path d="M8 36h40M8 52h40"/><path d="M28 40c3 4 5 6 5 9a5 5 0 0 1-10 0c0-3 2-5 5-9z"/></svg></div>
  <h3>Bottles</h3><p>Lorem ipsum dolor sit amet, consectetur<br>adipiscing elit sed do eiusmod tempor<br>incididunt ut labore et.</p>
</div>
<div class="prod" style="left:480px">
  <div class="ring" style="border-color:#0b8fd0"><svg width="44" height="80" viewBox="0 0 44 80" fill="none" stroke="#0d4ea8" stroke-width="2.2"><path d="M12 4h20v24H12z"/><path d="M12 12h20M12 20h20"/><rect x="5" y="30" width="34" height="46" rx="3"/><path d="M10 40h24v8H10z"/><path d="M22 56c2 3 4 5 4 7a4 4 0 0 1-8 0c0-2 2-4 4-7z"/></svg></div>
  <h3>Dispensers</h3><p>Lorem ipsum dolor sit amet, consectetur<br>adipiscing elit sed do eiusmod tempor<br>incididunt ut labore et.</p>
</div>
<div class="prod" style="left:746px">
  <div class="ring" style="border-color:#5b8fd0"><svg width="70" height="70" viewBox="0 0 70 70" fill="none" stroke="#3f7fd0" stroke-width="2.2"><rect x="14" y="6" width="14" height="8" rx="2"/><rect x="8" y="16" width="28" height="48" rx="5"/><path d="M22 32c4 6 7 9 7 13a7 7 0 0 1-14 0c0-4 3-7 7-13z"/><circle cx="46" cy="46" r="10"/><path d="M56 8c3 5 5 7 5 10a5 5 0 0 1-10 0c0-3 2-5 5-10z"/></svg></div>
  <h3>Water Refilling</h3><p>Lorem ipsum dolor sit amet, consectetur<br>adipiscing elit sed do eiusmod tempor<br>incididunt ut labore et.</p>
</div>

<!-- process -->
<h2 class="abs process-title">A Higher Standard of Water<br>Delivered Process</h2>
<div class="step" style="left:230px">
  <div class="step-head"><span class="step-label">STEP</span><span class="step-num">01</span></div>
  <h3>Order Your Bottle</h3>
  <p>Foresee the pain and trouble that are bound to ensue and equal blame fail.</p>
  <div class="step-icon"><i></i></div>
</div>
<div class="step" style="left:483px">
  <div class="step-head"><span class="step-label">STEP</span><span class="step-num">02</span></div>
  <h3>Touchless Packing</h3>
  <p>Our power of choice is untrammelled and when nothing prevents our being able.</p>
  <div class="step-icon"><i></i></div>
</div>
<div class="step" style="left:736px">
  <div class="step-head"><span class="step-label">STEP</span><span class="step-num">03</span></div>
  <h3>On Time Deliver</h3>
  <p>Business will frequently occur that who pleasures have to be repudiated &amp; accepted.</p>
  <div class="step-icon"><i></i></div>
</div>

<!-- showcase -->
<p class="abs big-word">100% PURE WATER. NATURAL</p>
<div class="abs show-disc"></div>
<div class="abs show-art" role="img" aria-label="Branded bottle and water jug with ice cubes and mint leaves"></div>

<!-- footer -->
<svg class="abs footer-wave" viewBox="0 0 1200 40" preserveAspectRatio="none"><path d="M0 18C60 8 120 28 180 18S300 8 360 18 480 28 540 18 660 8 720 18 840 28 900 18 1020 8 1080 18 1160 26 1200 18V40H0Z" fill="#1b2460"/></svg>
<footer class="abs footer"></footer>

<p class="abs cta">Please <em>Call Us</em> to Take an Extraordinary Service</p>
<a class="abs cta-btn"><span class="dot" style="width:24px;height:24px;background:#0b6fd0"><svg width="12" height="12" viewBox="0 0 24 24"><path d="M6.6 10.8a15.1 15.1 0 0 0 6.6 6.6l2.2-2.2c.3-.3.7-.4 1-.2 1.1.4 2.3.6 3.6.6.6 0 1 .4 1 1V20c0 .6-.4 1-1 1A17 17 0 0 1 3 4c0-.6.4-1 1-1h3.5c.6 0 1 .4 1 1 0 1.3.2 2.5.6 3.6.1.3 0 .7-.2 1z" fill="#fff"/></svg></span>555-014-2730</a>
<svg class="abs" style="left:230px;top:2766px" width="740" height="14" viewBox="0 0 740 14"><path d="M0 7q10-7 20 0t20 0 20 0 20 0 20 0 20 0 20 0 20 0 20 0 20 0 20 0 20 0 20 0 20 0 20 0 20 0 20 0 20 0 20 0 20 0 20 0 20 0 20 0 20 0 20 0 20 0 20 0 20 0 20 0 20 0 20 0 20 0 20 0 20 0 20 0 20 0 20 0" fill="none" stroke="#7BADD7" stroke-width="1.2"/></svg>

<div class="abs foot-brand">Brookvale<br>Fill House</div>
<p class="abs foot-text" style="left:230px;top:2882px;width:190px">Lorem ipsum dolor sit amet, consectet adipiscing elit, sed do eiusmod</p>
<div class="abs foot-row foot-text" style="left:230px;top:2924px"><svg width="10" height="13" viewBox="0 0 10 13"><path d="M5 0a5 5 0 0 1 5 5c0 4-5 8-5 8S0 9 0 5a5 5 0 0 1 5-5z" fill="#2aa6f0"/><circle cx="5" cy="5" r="1.8" fill="#1b2460"/></svg><span>2280 W. Alder Crest Rd., Ste. 4<br>Fairhaven, AZ 85000</span></div>
<div class="abs foot-row foot-text" style="left:230px;top:2958px"><svg width="10" height="8" viewBox="0 0 10 8"><rect width="10" height="8" rx="1" fill="#2aa6f0"/><path d="M0 1l5 4 5-4" stroke="#1b2460" fill="none"/></svg><span>support@brookvalebottleworks.com</span></div>
<div class="abs foot-row foot-text" style="left:230px;top:2976px"><svg width="10" height="10" viewBox="0 0 24 24"><path d="M6.6 10.8a15.1 15.1 0 0 0 6.6 6.6l2.2-2.2c.3-.3.7-.4 1-.2 1.1.4 2.3.6 3.6.6.6 0 1 .4 1 1V20c0 .6-.4 1-1 1A17 17 0 0 1 3 4c0-.6.4-1 1-1h3.5c.6 0 1 .4 1 1 0 1.3.2 2.5.6 3.6.1.3 0 .7-.2 1z" fill="#2aa6f0"/></svg><span>(555) 014-2730</span></div>

<h4 class="abs foot-h" style="left:489px;top:2831px">QUICK LINKS</h4>
<ul class="abs foot-list" style="left:489px;top:2870px"><li>Home</li><li>About Us</li><li>Our Product</li><li>Blog</li><li>Contact</li></ul>
<h4 class="abs foot-h" style="left:648px;top:2831px">SERVICES</h4>
<ul class="abs foot-list" style="left:648px;top:2870px"><li>Bottle</li><li>Dispensers</li><li>Water Refilling</li></ul>
<h4 class="abs foot-h" style="left:793px;top:2831px">WORK HOURS</h4>
<ul class="abs foot-list" style="left:793px;top:2870px"><li style="height:22px">Tuesday–Friday 9am–6pm</li><li style="height:22px">Saturday &amp; Sunday 10am–5pm</li><li>Closed on Mondays</li></ul>
<span class="abs social" style="left:793px;top:2962px;width:23px;height:23px;background:#fff"></span>
<span class="abs social" style="left:826px;top:2962px;width:23px;height:23px;background:#fff"></span>

<p class="abs copy">Copyright © 2026 brookvalebottleworks.com. All Rights Reserved.</p>

</body>
</html>
```